Stationary for Clinical Psychologist and Consultant
Morlek Psychological Consulting
Stationary for Clinical Psychologist and Consultant - Health
Creative Brief
Professional
Gerald P. Hensow, Psy.D.
Licensed Clinical Psychologist
418 Brackenfield Road Suite B Hawthorn Woods, IL 60093
ghensow@morlekpsyconsult.example
www.morlekpsyconsult.example
Institute for Renewal and Steadfast Growth

```html
<!DOCTYPE html>
<html lang="en">
<head>
<meta charset="utf-8">
<title>Morlek Psychological Consulting — Stationery</title>
<link rel="stylesheet" href="https://fonts.googleapis.com/css2?family=Cinzel:wght@500&family=Lato:wght@400;700&display=swap">
<style>
  :root{
    --canvas:#f0f0f0;
    --paper:#ffffff;
    --ink:#0b0b0b;
    --band:#0d0d0f;
    --rule:#c9c9c9;
    --muted:#6a6a6a;
    --accent:#1f3f9a;
    --accent-light:#6d8fd8;
    --silver:#b8bcc4;
  }
  *{box-sizing:border-box;margin:0;padding:0}
  html,body{width:1200px;height:559px;overflow:hidden;background:var(--canvas);font-family:"Lato",sans-serif;color:var(--ink)}
  .canvas{position:relative;width:1200px;height:559px}
  .sheet{position:absolute;background:var(--paper);box-shadow:0 1px 3px rgba(0,0,0,.25)}
  .band{background:var(--band);display:flex;align-items:center;justify-content:center}
  .brand{display:flex;align-items:center;gap:6px;color:#fff;font-family:"Cinzel",serif;font-weight:500;letter-spacing:.06em;text-transform:uppercase;line-height:1.2;text-align:center}
  .brand-dot{width:9px;height:9px;border-radius:50%;background:var(--accent-light);flex:none}
  .band-header{position:absolute;left:0;top:0;width:100%;height:80px}
  .band-header .brand{font-size:9.5px;flex-direction:column;gap:4px}
  .footer-line{position:absolute;left:0;right:0;bottom:12px;text-align:center;font-size:4.8px;color:var(--muted);line-height:1.6}
  /* fax */
  .fax-title{position:absolute;right:18px;top:98px;font-weight:700;font-size:15px;letter-spacing:.04em}
  .fax-form{position:absolute;left:18px;right:18px;top:124px;display:grid;grid-template-columns:1fr 1fr;column-gap:22px}
  .fax-field{display:flex;align-items:flex-end;height:15px;border-bottom:1px solid var(--rule);font-size:5.5px;color:#333}
  .fax-field span{width:30px}
  .fax-checks{position:absolute;left:18px;right:18px;top:212px;display:flex;justify-content:space-between;font-size:5.5px;color:#333}
  .fax-checks label{display:flex;align-items:center;gap:3px}
  .fax-checks i{width:5px;height:5px;border:1px solid #555;display:inline-block}
  .fax-divider{position:absolute;left:18px;right:18px;top:228px;border-top:1px solid var(--rule)}
  /* cards */
  .card{position:absolute;background:var(--band);border-radius:5px;overflow:hidden}
  .card-front .brand{position:absolute;left:0;right:0;top:30px;font-size:6.5px;flex-direction:column;gap:2px}
  .card-stripe{position:absolute;left:0;right:0;top:70px;height:14px;background:linear-gradient(90deg,var(--silver),#eef0f4 50%,var(--silver))}
  .card-back{background:linear-gradient(180deg,#0d0d14 0%,#0d0d14 55%,var(--accent) 100%)}
  .card-back .brand{position:absolute;left:0;right:0;top:42px;font-size:6.5px;flex-direction:column;gap:2px}
  .card-back .contact{position:absolute;left:0;right:0;bottom:10px;text-align:center;font-size:4.6px;color:#d6dcef}
  /* envelope */
  .envelope .band{position:absolute;left:0;top:0;width:100%;height:62px;justify-content:flex-start;padding-left:40px}
  .envelope .brand{font-size:7px;flex-direction:column;align-items:flex-start;gap:2px;text-align:left}
  .slip .band{position:absolute;left:0;top:0;width:100%;height:58px;justify-content:flex-start;padding-left:40px}
  .slip .brand{font-size:7px;flex-direction:column;align-items:flex-start;gap:2px;text-align:left}
  .return-address{position:absolute;left:20px;top:72px;font-size:4.8px;color:var(--muted);line-height:1.6}
  .slip-footer{position:absolute;right:22px;bottom:10px;font-size:4.6px;color:var(--muted)}
</style>
</head>
<body>
<main class="canvas">

  <!-- Fax sheet -->
  <section class="sheet fax" style="left:41px;top:29px;width:350px;height:521px">
    <header class="band band-header">
      <div class="brand"><span class="brand-dot"></span><span>Morlek Psychological<br>Consulting</span></div>
    </header>
    <div class="fax-title">FAX</div>
    <div class="fax-form">
      <div class="fax-field"><span>To:</span></div><div class="fax-field"><span>From:</span></div>
      <div class="fax-field"><span>Fax:</span></div><div class="fax-field"><span>Pages:</span></div>
      <div class="fax-field"><span>Phone:</span></div><div class="fax-field"><span>Date:</span></div>
      <div class="fax-field"><span>Re:</span></div><div class="fax-field"><span>CC:</span></div>
    </div>
    <div class="fax-checks">
      <label><i></i>Urgent</label><label><i></i>For Review</label><label><i></i>Please Comment</label><label><i></i>Please Reply</label><label><i></i>Please Recycle</label>
    </div>
    <div class="fax-divider"></div>
    <p class="footer-line">418 Brackenfield Road Suite B Hawthorn Woods, IL 60093<br>(847) 555-0148 · F (847) 555-0149 · www.morlekpsyconsult.example</p>
  </section>

  <!-- Letterhead -->
  <section class="sheet letterhead" style="left:413px;top:29px;width:350px;height:521px">
    <header class="band band-header">
      <div class="brand"><span class="brand-dot"></span><span>Morlek Psychological<br>Consulting</span></div>
    </header>
    <p class="footer-line">418 Brackenfield Road Suite B Hawthorn Woods, IL 60093<br>(847) 555-0148 · ghensow@morlekpsyconsult.example · www.morlekpsyconsult.example</p>
  </section>

  <!-- Business card front -->
  <section class="card card-front" style="left:806px;top:29px;width:185px;height:108px">
    <div class="brand"><span class="brand-dot"></span><span>Morlek Psychological<br>Consulting</span></div>
    <div class="card-stripe"></div>
  </section>

  <!-- Business card back -->
  <section class="card card-back" style="left:1006px;top:29px;width:185px;height:108px">
    <div class="brand"><span class="brand-dot"></span><span>Morlek Psychological<br>Consulting</span></div>
    <p class="contact">Gerald P. Hensow, Psy.D. · Licensed Clinical Psychologist</p>
  </section>

  <!-- Envelope -->
  <section class="sheet envelope" style="left:775px;top:265px;width:415px;height:120px">
    <div class="band">
      <div class="brand"><span class="brand-dot"></span><span>Morlek Psychological<br>Consulting</span></div>
    </div>
  </section>

  <!-- Envelope face / compliments slip -->
  <section class="sheet slip" style="left:775px;top:398px;width:415px;height:152px">
    <div class="band">
      <div class="brand"><span class="brand-dot"></span><span>Morlek Psychological<br>Consulting</span></div>
    </div>
    <p class="return-address">418 Brackenfield Road Suite B<br>Hawthorn Woods, IL 60093</p>
    <p class="slip-footer">Institute for Renewal and Steadfast Growth</p>
  </section>

</main>
</body>
</html>
```